vTend Cookbook Cover

I need a design (front and back) for a cookbook cover. Our partners are looking for a few ideas to pick from.
You can see the style for one of the cookbooks we currently carry - uploaded with this brief.
This cookbook is a little different than most cookbooks out there. It is a cancer-fighting cookbook but we don't want it to be so cancer focused that people who don't have cancer will not buy. The book starts out with a section for Foods that Help, then goes to another section called Foods that Hurt. Then, we provide a Recipes section from the ingredients found in Foods that Help. Finally, the last section is called Beyond the Plate and deals with healthy lifestyle habits. You can see a rough draft of the content of the book at the link below. Please keep in mind that the current covers you see are not at all what we want. These were just put there to fill in the space.
Link for cookbook content: https://www.filecrate-share.net/s/4kq29lmzwpbtnxv/The%20Bright%20Bowl%20-%20EDITED.pdf?dl=0
The title: The Bright Bowl
Subtitle: Fighting Cancer One Meal at a Time
Author: Mirel Ostvan
The company that puts the book out is vTend. It would be nice to have the logo somewhere small. Logo can be found here: https://www.filecrate-share.net/s/hrp61wetcozuv3m/vTend%20Logo%20%26%20Guidelines.zip?dl=0
Like "Hand Over A Warmer Day" attached to this brief, we do NOT want something somber but more on the bright side. Just make it look nice and fresh. It would also be nice to somehow incorporate the concept of the cancer ribbon or a silhouette of it in a way that is not upfront but can still be acknowledge. No need for it to be pink and if that does not work, than it's better just to leave it out.
For the back cover, you can design it but simply leave room for us to fill in some text. No need for a spine design as it will be spiral bound.
The file must be designed and saved in PHOTOSHOP format.
According to the designer, the dimensions are:
207mm x 270mm + 5mm bleed
If you want to use the recipe pictures somehow in the cover, just snatch a picture from the content PDF and we can always replace it with the original larger file at a later time. Unfortunately, I don't have the pictures uploaded in filecrate.

```html
<!DOCTYPE html>
<html lang="en">
<head>
<meta charset="utf-8">
<title>The Bright Bowl — Cover</title>
<link rel="stylesheet" href="https://fonts.googleapis.com/css2?family=Marcellus&family=Quicksand:wght@400&family=Comfortaa:wght@300;400&display=swap">
<style>
  :root {
    --backdrop: #ececec;
    --paper: #ffffff;
    --ink: #1e1e1e;
    --ink-soft: #3c3c3c;
    --food-butter: #f3d36a;
    --food-cream: #efe6d6;
    --food-milk: #f6f3ee;
    --food-berry: #b4474f;
    --food-toast: #c99a5e;
    --food-orange: #f0a03c;
  }
  html, body {
    margin: 0;
    padding: 0;
    width: 1030px;
    height: 1200px;
    overflow: hidden;
    background: var(--backdrop);
  }
  .cover {
    position: absolute;
    left: 75px;
    top: 26px;
    width: 880px;
    height: 1148px;
    background: var(--paper);
    overflow: hidden;
    box-shadow: 0 2px 10px rgba(0,0,0,0.08);
  }
  .food-photo {
    position: absolute;
    left: 0;
    top: 255px;
    width: 880px;
    height: 893px;
    background:
      radial-gradient(ellipse 180px 140px at 300px 300px, rgba(180,71,79,0.45), transparent 70%),
      radial-gradient(ellipse 220px 200px at 760px 70px, rgba(240,160,60,0.75), transparent 70%),
      radial-gradient(ellipse 260px 220px at 700px 640px, rgba(201,154,94,0.85), transparent 70%),
      radial-gradient(ellipse 200px 220px at 110px 520px, rgba(243,211,106,0.9), transparent 70%),
      radial-gradient(ellipse 160px 160px at 320px 780px, rgba(240,160,60,0.55), transparent 70%),
      linear-gradient(180deg, var(--food-cream) 0%, var(--food-milk) 45%, var(--food-cream) 100%);
  }
  .stripe {
    position: absolute;
    top: 255px;
    bottom: 0;
    background: var(--paper);
  }
  .title {
    position: absolute;
    left: 0;
    top: 0;
    width: 880px;
    height: 300px;
    color: var(--ink);
  }
  .title-article {
    position: absolute;
    left: 34px;
    top: 70px;
    font-family: "Quicksand", sans-serif;
    font-size: 64px;
    letter-spacing: 6px;
    color: var(--ink);
    line-height: 1;
  }
  .title-main {
    position: absolute;
    left: 36px;
    top: 96px;
    font-family: "Marcellus", serif;
    font-size: 150px;
    letter-spacing: 44px;
    line-height: 1;
    color: var(--ink);
  }
  .title-end {
    position: absolute;
    right: 24px;
    top: 178px;
    font-family: "Quicksand", sans-serif;
    font-size: 98px;
    letter-spacing: 10px;
    line-height: 1;
    color: var(--ink-soft);
  }
  .subtitle {
    position: absolute;
    left: 242px;
    top: 300px;
    width: 59px;
    writing-mode: vertical-rl;
    font-family: "Comfortaa", sans-serif;
    font-weight: 300;
    font-size: 28px;
    letter-spacing: 9px;
    line-height: 59px;
    color: var(--ink);
    white-space: nowrap;
  }
  .author {
    position: absolute;
    left: 516px;
    bottom: 40px;
    width: 66px;
    writing-mode: vertical-rl;
    transform: rotate(180deg);
    font-family: "Comfortaa", sans-serif;
    font-weight: 300;
    font-size: 26px;
    letter-spacing: 5px;
    line-height: 66px;
    color: var(--ink);
    white-space: nowrap;
  }
</style>
</head>
<body>
  <main class="cover">
    <div class="food-photo" role="img" aria-label="Bright breakfast spread: muesli jar, yogurt bowl with berries, fruit salad, orange slices, scrambled eggs with bacon, butter, jams and toast with jam on a white table"></div>

    <div class="stripe" style="left:19px;width:7px"></div>
    <div class="stripe" style="left:36px;width:15px"></div>
    <div class="stripe" style="left:96px;width:17px"></div>
    <div class="stripe" style="left:162px;width:34px"></div>
    <div class="stripe stripe-subtitle" style="left:242px;width:59px"></div>
    <div class="stripe stripe-author" style="left:516px;width:66px"></div>
    <div class="stripe" style="left:636px;width:8px"></div>
    <div class="stripe" style="left:705px;width:7px"></div>
    <div class="stripe" style="left:749px;width:9px"></div>
    <div class="stripe" style="left:804px;width:6px"></div>
    <div class="stripe" style="left:829px;width:8px"></div>

    <h1 class="title">
      <span class="title-main">BRIGHT</span>
      <span class="title-article">The</span>
      <span class="title-end">Bowl</span>
    </h1>

    <p class="subtitle">fighting cancer one meal at a time</p>
    <p class="author">by Mirel Ostvan</p>
  </main>
</body>
</html>
```